Vapora Deck

An e-commerce website targeting B2B and B2C customers.

High level requirements are:

Selling Tobacco Hooka Products
Home Page
English/Arabic
Main Rotating Banner
Login / Registration
Multiple delivery address
Temporary delivery address
Online payment
My account page / Order History / addresses / Payment info
Contact us page
About
Reviews 5 star rating system
Social media share buttons and email on each product page
Purchase quantity
Recommendations
Information and specifications on each product
Main search and tab bar at the top remains at the top when scrolling down
website should work seamlessly across all devise browsers adapting to the screen size mobile friendly
Whole sale page and login
Individual brand pages (i.e. Glintmoor, Tova, Doren…) accessible from the first page drop down menu
Single product endless scrolling design no pages, with search, filter and sort menu at the top and how many products found
Design should be clean / clear / uncluttered / simple / easy / light / friendly and straight to the point
Currency convention automatically through I.P address

Best example i wouldn’t mind and exact copy is http://brindle.pelvorexample.com

Industry/Entity Type

E-Commerce

```html
<!DOCTYPE html>
<html lang="en">
<head>
<meta charset="utf-8">
<title>Vapora Deck — Our Products</title>
<link rel="stylesheet" href="https://fonts.googleapis.com/css2?family=Open+Sans:wght@300;400;600&display=swap">
<style>
  :root {
    --ink: #333333;
    --muted: #6a6a6a;
    --accent: #d81e1e;
    --rule: #e3e3e3;
    --toolbar: #f0f0f0;
    --footer: #242424;
    --footer-base: #1a1a1a;
    --footer-text: #bdbdbd;
    --white: #ffffff;
  }
  * { box-sizing: border-box; margin: 0; padding: 0; }
  html, body { width: 708px; height: 1200px; overflow: hidden; background: var(--white); }
  body { position: relative; font-family: "Open Sans", Arial, sans-serif; color: var(--ink); }
  .abs { position: absolute; }

  /* header */
  .site-header { position: absolute; left: 0; top: 0; width: 708px; height: 59px; background: var(--white); }
  .brand { position: absolute; left: 76px; top: 19px; font-size: 16px; font-weight: 600; color: var(--accent); letter-spacing: 0.2px; }
  .main-nav a { position: absolute; top: 26px; font-size: 8.5px; color: var(--ink); text-decoration: none; letter-spacing: 0.2px; }
  .lang-select { position: absolute; left: 577px; top: 22px; width: 61px; height: 18px; border: 1px solid #cfcfcf; font-size: 7.5px; display: flex; align-items: center; padding-left: 5px; gap: 4px; color: var(--ink); }
  .lang-flag { width: 11px; height: 8px; background: #2b3f8c; }
  .lang-caret { margin-left: auto; margin-right: 5px; width: 0; height: 0; border-left: 3px solid transparent; border-right: 3px solid transparent; border-top: 4px solid #666; }

  /* hero */
  .hero { position: absolute; left: 0; top: 59px; width: 708px; height: 163px;
    background: linear-gradient(90deg, #2a1b10 0%, #5a3a1e 25%, #a6773e 48%, #7b5330 70%, #3a2616 100%); }
  .hero-title { position: absolute; left: 74px; top: 68px; font-size: 16px; font-weight: 400; color: var(--white); letter-spacing: 0.3px; }
  .hero-sub { position: absolute; left: 77px; top: 89px; font-size: 7.5px; color: #f2e8dc; letter-spacing: 0.2px; }

  /* toolbar */
  .catalog-toolbar { position: absolute; left: 76px; top: 248px; width: 561px; height: 41px; background: var(--toolbar); font-size: 8px; color: var(--muted); letter-spacing: 0.2px; }
  .toolbar-item { position: absolute; top: 0; height: 41px; display: flex; align-items: center; gap: 6px; }
  .toolbar-sep { position: absolute; top: 0; width: 1px; height: 41px; background: #dcdcdc; }
  .toolbar-item svg { stroke: #555; fill: none; stroke-width: 1.2; }

  /* products */
  .product-image { position: absolute; width: 70px; border-radius: 4px;
    background: radial-gradient(ellipse at 50% 60%, #c9d3e6 0%, #eef1f6 60%, #ffffff 100%); }
  .product-name { position: absolute; font-size: 8px; color: var(--muted); letter-spacing: 0.2px; }
  .product-price { position: absolute; font-size: 8px; color: var(--accent); text-align: right; width: 60px; }
  .row-rule { position: absolute; left: 72px; width: 566px; height: 1px; background: var(--rule); }

  /* footer */
  .site-footer { position: absolute; left: 0; top: 993px; width: 708px; height: 167px;
    background: repeating-linear-gradient(45deg, var(--footer) 0 2px, #282828 2px 4px); }
  .footer-col { position: absolute; top: 36px; }
  .footer-col h3 { font-size: 11px; font-weight: 400; color: var(--white); margin-bottom: 5px; letter-spacing: 0.2px; }
  .footer-col li { list-style: none; font-size: 7px; line-height: 14.4px; color: var(--footer-text); padding-left: 2px; }
  .social { display: flex; gap: 2px; margin-top: 2px; }
  .social span { width: 16px; height: 16px; border-radius: 50%; background: var(--white); }
  .footer-base { position: absolute; left: 0; top: 1160px; width: 708px; height: 40px; background: var(--footer-base); }
  .copyright { position: absolute; left: 64px; top: 15px; font-size: 7px; color: var(--footer-text); }
</style>
</head>
<body>

<header class="site-header">
  <div class="brand">Vapora Deck</div>
  <nav class="main-nav">
    <a style="left:223px">ABOUT US</a>
    <a style="left:286px">PRODUCTS</a>
    <a style="left:353px">BLOG</a>
    <a style="left:397px">BUY NOW</a>
    <a style="left:458px">SUPPORT</a>
    <a style="left:518px">CONTACT</a>
  </nav>
  <div class="lang-select"><span class="lang-flag"></span>English<span class="lang-caret"></span></div>
</header>

<section class="hero" role="img" aria-label="Banner photo of a woman smoking a hookah in a warmly lit lounge">
  <h1 class="hero-title">OUR PRODUCTS</h1>
  <p class="hero-sub">SUSPENDISSE VULPUTATE ALIQUAM</p>
</section>

<div class="catalog-toolbar">
  <div class="toolbar-item" style="left:22px">HOOKAH</div>
  <div class="toolbar-item" style="left:145px">
    <svg width="13" height="13" viewBox="0 0 13 13"><circle cx="5.5" cy="5.5" r="4.2"/><line x1="8.6" y1="8.6" x2="12" y2="12"/></svg>SEARCH
  </div>
  <div class="toolbar-sep" style="left:210px"></div>
  <div class="toolbar-item" style="left:229px">
    <svg width="13" height="12" viewBox="0 0 13 12" style="fill:#555;stroke:none"><circle cx="2" cy="2" r="1.5"/><circle cx="6.5" cy="2" r="1.5"/><circle cx="11" cy="2" r="1.5"/><circle cx="4.2" cy="6" r="1.5"/><circle cx="8.8" cy="6" r="1.5"/><circle cx="6.5" cy="10" r="1.5"/></svg>FILTER
  </div>
  <div class="toolbar-sep" style="left:288px"></div>
  <div class="toolbar-item" style="left:304px">
    <svg width="16" height="14" viewBox="0 0 16 14"><line x1="3" y1="2" x2="3" y2="13"/><polyline points="1,11 3,13 5,11"/><line x1="7" y1="5" x2="14" y2="5"/><line x1="7" y1="8" x2="12" y2="8"/><line x1="7" y1="11" x2="10" y2="11"/><line x1="14" y1="1" x2="14" y2="4"/></svg>SORT BY
  </div>
  <div class="toolbar-sep" style="left:382px"></div>
  <div class="toolbar-item" style="left:404px">
    <svg width="12" height="12" viewBox="0 0 12 12"><line x1="4" y1="0" x2="4" y2="12"/><line x1="8" y1="0" x2="8" y2="12"/><line x1="0" y1="4" x2="12" y2="4"/><line x1="0" y1="8" x2="12" y2="8"/></svg>GRID
  </div>
  <div class="toolbar-sep" style="left:463px"></div>
  <div class="toolbar-item" style="left:483px">
    <svg width="16" height="10" viewBox="0 0 16 10" style="stroke-width:2"><line x1="0" y1="1" x2="16" y2="1"/><line x1="0" y1="5" x2="16" y2="5"/><line x1="0" y1="9" x2="16" y2="9"/></svg>LIST
  </div>
</div>

<main class="product-grid">
  <!-- row 1 -->
  <div class="product-image" role="img" aria-label="Hookah product photo" style="left:125px;top:332px;height:84px"></div>
  <div class="product-image" role="img" aria-label="Hookah product photo" style="left:319px;top:332px;height:84px"></div>
  <div class="product-image" role="img" aria-label="Hookah product photo" style="left:507px;top:332px;height:84px"></div>
  <span class="product-name" style="left:78px;top:429px">PRODUCT TITTLE</span><span class="product-price" style="left:174px;top:429px">$ 48.99</span>
  <span class="product-name" style="left:278px;top:429px">PRODUCT TITTLE</span><span class="product-price" style="left:374px;top:429px">$ 48.99</span>
  <span class="product-name" style="left:476px;top:429px">PRODUCT TITTLE</span><span class="product-price" style="left:573px;top:429px">$ 48.99</span>
  <div class="row-rule" style="top:469px"></div>

  <!-- row 2 -->
  <div class="product-image" role="img" aria-label="Hookah product photo" style="left:127px;top:494px;height:88px"></div>
  <div class="product-image" role="img" aria-label="Hookah product photo" style="left:321px;top:494px;height:88px"></div>
  <div class="product-image" role="img" aria-label="Hookah product photo" style="left:511px;top:494px;height:88px"></div>
  <span class="product-name" style="left:78px;top:597px">PRODUCT TITTLE</span><span class="product-price" style="left:174px;top:597px">$ 48.99</span>
  <span class="product-name" style="left:278px;top:597px">PRODUCT TITTLE</span><span class="product-price" style="left:374px;top:597px">$ 48.99</span>
  <span class="product-name" style="left:476px;top:597px">PRODUCT TITTLE</span><span class="product-price" style="left:573px;top:597px">$ 48.99</span>
  <div class="row-rule" style="top:635px"></div>

  <!-- row 3 -->
  <div class="product-image" role="img" aria-label="Hookah product photo" style="left:130px;top:650px;height:84px"></div>
  <div class="product-image" role="img" aria-label="Hookah product photo" style="left:326px;top:650px;height:84px"></div>
  <div class="product-image" role="img" aria-label="Hookah product photo" style="left:508px;top:650px;height:84px"></div>
  <span class="product-name" style="left:78px;top:756px">PRODUCT TITTLE</span><span class="product-price" style="left:174px;top:756px">$ 48.99</span>
  <span class="product-name" style="left:278px;top:756px">PRODUCT TITTLE</span><span class="product-price" style="left:374px;top:756px">$ 48.99</span>
  <span class="product-name" style="left:476px;top:756px">PRODUCT TITTLE</span><span class="product-price" style="left:573px;top:756px">$ 48.99</span>
  <div class="row-rule" style="top:795px"></div>

  <!-- row 4 -->
  <div class="product-image" role="img" aria-label="Hookah product photo" style="left:127px;top:820px;height:90px"></div>
  <div class="product-image" role="img" aria-label="Hookah product photo" style="left:319px;top:820px;height:90px"></div>
  <div class="product-image" role="img" aria-label="Hookah product photo" style="left:507px;top:820px;height:90px"></div>
  <span class="product-name" style="left:78px;top:929px">PRODUCT TITTLE</span><span class="product-price" style="left:174px;top:929px">$ 48.99</span>
  <span class="product-name" style="left:278px;top:929px">PRODUCT TITTLE</span><span class="product-price" style="left:374px;top:929px">$ 48.99</span>
  <span class="product-name" style="left:476px;top:929px">PRODUCT TITTLE</span><span class="product-price" style="left:573px;top:929px">$ 48.99</span>
</main>

<footer class="site-footer">
  <div class="footer-col" style="left:74px">
    <h3>COMPANY</h3>
    <ul><li>Aliquam nec erat</li><li>At purus cursus</li><li>Interdum Vestibulum</li><li>Ligula augue</li><li>Bibendum accumsan</li></ul>
  </div>
  <div class="footer-col" style="left:193px">
    <h3>FEATURES</h3>
    <ul><li>Aliquam nec erat</li><li>At purus cursus</li><li>Interdum Vestibulum</li><li>Ligula augue</li><li>Bibendum accumsan</li></ul>
  </div>
  <div class="footer-col" style="left:309px">
    <h3>ABOUT</h3>
    <ul><li>Aliquam nec erat</li><li>At purus cursus</li><li>Interdum Vestibulum</li><li>Ligula augue</li><li>Bibendum accumsan</li></ul>
  </div>
  <div class="footer-col" style="left:424px">
    <h3>SERVICES</h3>
    <ul><li>Aliquam nec erat</li><li>At purus cursus</li><li>Interdum Vestibulum</li><li>Ligula augue</li><li>Bibendum accumsan</li></ul>
  </div>
  <div class="footer-col" style="left:530px">
    <h3>GET IN TOUCH</h3>
    <div class="social" aria-label="Social links"><span></span><span></span><span></span><span></span></div>
  </div>
</footer>
<div class="footer-base">
  <p class="copyright">© 2014 Company Name &nbsp;All right reserved &nbsp;Term of Use</p>
</div>

</body>
</html>
```